I am writing a book called "JOY FINDS THE WAY "

I NEED A BOOK COVER FOR MY BOOK" JOY FINDS THE WAY"
so what was the question? " ( this in smaller font)

"Joy Finds the Way " will need to designed to eventually be a logo , banner and business card
COLOURS MAINLY ORANGE AND WHITE (with accents bright colour )

THE BOOK IS MY LAUGHTER JOURNEY AS A PERFORMER AND ADVENTURE INDIA LEARNING ABOUT LAUGHTER YOGA WHICH I WILL BE TEACHING

I do not want photos on the front cover ..
The look could be modern and eye-catching
I have also just been to India to learn Laughing Yoga with Dr Rohit Venkatesh

Thank-you so much everyone for your brilliant designs . i am overwhelmed with your talent . i hope to work with you all again soon ! Moira  

Target Market(s)

"Adults based in western speaking countries aged 25 to 60 that want to learn to laugh more
Also this book will be sold at my conference workshops

Industry/Entity Type

Business

Requirements
Must have
• ORANGE AND WHITE
CAN HAVE AQUA , HOT PINK , LIME GREEN, YELLOW ACCENTS

THESE WILL BE DIFFERENT AREAS WILL COVERING IN MY BOOK
EG LAUGHTER NAD BREAT CANCER ( PINK)
LAUGHTER NAD DEPRESSION ( BLUE)
LAUGHTER AND KIDS ( YELLOW)

NO Photos on front cover
Should not have
• No photos

```html
<!DOCTYPE html>
<html lang="en">
<head>
<meta charset="utf-8">
<title>Joy Finds the Way – Book Cover</title>
<link rel="stylesheet" href="https://fonts.googleapis.com/css2?family=Anton&display=swap">
<style>
  :root {
    --hot-pink: #ec1c7a;
    --aqua: #1fb3ad;
    --white: #ffffff;
    --sun-yellow: #fff35a;
    --sun-orange: #f7941d;
    --sun-deep: #f26a2a;
    --sun-pink: #f0459a;
  }
  html, body {
    margin: 0;
    padding: 0;
    width: 800px;
    height: 1200px;
    overflow: hidden;
  }
  .cover {
    position: relative;
    width: 800px;
    height: 1200px;
    overflow: hidden;
    font-family: "Anton", "Arial Narrow", sans-serif;
  }
  .cover__burst {
    position: absolute;
    inset: 0;
    background:
      radial-gradient(circle at 50% 46%,
        #fffef0 0%,
        var(--sun-yellow) 14%,
        #ffc93c 30%,
        var(--sun-orange) 50%,
        var(--sun-deep) 68%,
        var(--sun-pink) 100%);
  }
  .cover__title {
    position: absolute;
    inset: 0;
  }
  .cover__author {
    position: absolute;
    left: 283px;
    top: 1120px;
    width: 265px;
    height: 58px;
    border-radius: 14px;
    background: var(--aqua);
    color: var(--white);
    font-size: 38px;
    line-height: 58px;
    text-align: center;
    letter-spacing: 1px;
  }
</style>
</head>
<body>
<main class="cover">
  <div class="cover__burst" role="img" aria-label="Radiating sunburst of pink, orange and yellow rays around a bright glowing centre"></div>

  <svg class="cover__title" width="800" height="1200" viewBox="0 0 800 1200" aria-label="JOY FINDS THE WAY – so what was the question?">
    <g transform="rotate(-8 420 600)">
      <g class="title-backing" fill="var(--white)" stroke="var(--white)" stroke-width="44" stroke-linejoin="round">
        <text x="125" y="545" font-size="190" textLength="545" lengthAdjust="spacingAndGlyphs">JOY FINDS</text>
        <text x="120" y="705" font-size="205" textLength="150" lengthAdjust="spacingAndGlyphs">THE</text>
        <text x="295" y="668" font-size="122" textLength="420" lengthAdjust="spacingAndGlyphs">WAY</text>
        <rect x="285" y="690" width="420" height="70" rx="35"/>
      </g>
      <text class="title-main" x="125" y="545" font-size="190" fill="var(--hot-pink)" textLength="545" lengthAdjust="spacingAndGlyphs">JOY FINDS</text>
      <text class="title-lead" x="120" y="705" font-size="205" fill="var(--aqua)" textLength="150" lengthAdjust="spacingAndGlyphs">THE</text>
      <text class="title-tail" x="295" y="668" font-size="122" fill="var(--aqua)" textLength="420" lengthAdjust="spacingAndGlyphs">WAY</text>
      <rect class="subtitle-pill" x="285" y="690" width="420" height="70" rx="35" fill="var(--hot-pink)"/>
      <text class="subtitle" x="310" y="741" font-size="44" fill="var(--white)" textLength="370" lengthAdjust="spacingAndGlyphs">SO WHAT WAS THE QUESTION?</text>
    </g>
  </svg>

  <div class="cover__author">AUTHOR’S NAME</div>
</main>
</body>
</html>
```